Stylish Business Cards Wanted

- DOUBLE SIDED Design Required -

High end, edgy cards for a corporate and personal stylist. Must include logo,
Name: Belinda Forsey
Title: Director and Stylist
telephone : +61 8 8217 4592
email: belinda@thegarbledger.example
website: thegarbledger.example
Tag: Corporate Workwear & Uniform Specialist | Personal Stylist
Would like nice icons for telephone, email, website

Target Market(s)

Businesses wanting stylish uniforms, people wanting stylish wardrobes

Industry/Entity Type

Corporate Workwear Stylist

Contact Information for Business Card

I would like black, white and gold foiling incorporated in the design - possibly a touch of the other colours on my branding guide attached Name: Belinda Forsey Title: Director and Stylist telephone : +61 8 8217 4592 email: belinda@thegarbledger.example website: thegarbledger.example Tag: Corporate Workwear & Uniform Specialist | Personal Stylist Would like nice icons for telephone, email, website

Font styles to use
Other font styles liked:
• Raleway

Colors

Designer to choose colors to be used in the design.

Requirements
Must have
• Gold foil accents

```html
<!DOCTYPE html>
<html lang="en">
<head>
<meta charset="utf-8">
<title>The Garb Ledger — Business Cards</title>
<link rel="stylesheet" href="https://fonts.googleapis.com/css2?family=Montserrat:wght@600;700&family=Raleway:wght@500;600;700&display=swap">
<style>
  :root {
    --backdrop-dark: #161616;
    --backdrop-light: #2e2e2e;
    --card-black: #231f20;
    --card-white: #ffffff;
    --ink: #111111;
    --gold: #d4b15a;
    --divider: #c9c9c9;
  }
  * { box-sizing: border-box; margin: 0; padding: 0; }
  html, body {
    width: 1200px; height: 1200px; overflow: hidden;
  }
  body {
    background: radial-gradient(circle at 80% 15%, var(--backdrop-light), var(--backdrop-dark) 70%);
    display: flex; flex-direction: column; align-items: center; justify-content: center;
    gap: 60px;
    font-family: "Raleway", sans-serif;
  }
  .card {
    width: 820px; height: 480px; border-radius: 26px;
    position: relative; overflow: hidden;
    box-shadow: 0 18px 40px rgba(0,0,0,0.45);
  }
  /* Front */
  .card--front {
    background: var(--card-black);
    display: flex; align-items: center; justify-content: center;
  }
  .wordmark {
    font-family: "Raleway", sans-serif; font-weight: 600;
    color: var(--gold); text-transform: uppercase;
    letter-spacing: 0.22em; font-size: 44px;
  }
  /* Back */
  .card--back { background: var(--card-white); }
  .back-brand {
    position: absolute; left: 0; top: 0; width: 420px; height: 360px;
    display: flex; align-items: center; justify-content: center;
  }
  .back-brand .wordmark { color: var(--ink); font-size: 34px; }
  .back-divider {
    position: absolute; left: 420px; top: 70px; width: 1.5px; height: 230px;
    background: var(--divider);
  }
  .contact {
    position: absolute; left: 460px; top: 100px;
  }
  .contact__name {
    font-family: "Montserrat", sans-serif; font-weight: 700;
    font-size: 28px; color: var(--ink); text-transform: uppercase; letter-spacing: 0.02em;
  }
  .contact__title {
    font-family: "Montserrat", sans-serif; font-weight: 600;
    font-size: 16px; color: var(--gold); text-transform: uppercase; letter-spacing: 0.12em;
    margin-top: 2px; margin-bottom: 18px;
  }
  .contact__list { list-style: none; }
  .contact__item {
    display: flex; align-items: center; gap: 12px;
    font-family: "Montserrat", sans-serif; font-weight: 600;
    font-size: 17px; color: var(--ink); margin-bottom: 8px;
  }
  .contact__icon { width: 18px; height: 18px; flex: none; }
  .tagline-band {
    position: absolute; left: 50px; right: 50px; bottom: 40px; height: 46px;
    background: var(--card-black);
    display: flex; align-items: center; justify-content: center;
    font-family: "Raleway", sans-serif; font-weight: 700;
    font-size: 17px; color: var(--gold); letter-spacing: 0.12em; text-transform: uppercase;
  }
</style>
</head>
<body>
  <section class="card card--front" aria-label="Card front">
    <span class="wordmark">The Garb Ledger</span>
  </section>

  <section class="card card--back" aria-label="Card back">
    <div class="back-brand"><span class="wordmark">The Garb Ledger</span></div>
    <div class="back-divider"></div>
    <div class="contact">
      <p class="contact__name">Belinda Forsey</p>
      <p class="contact__title">Director and Stylist</p>
      <ul class="contact__list">
        <li class="contact__item">
          <svg class="contact__icon" viewBox="0 0 24 24" fill="none" stroke="var(--gold)" stroke-width="2" stroke-linecap="round" stroke-linejoin="round"><path d="M5 3h4l2 5-2.5 1.5a11 11 0 0 0 6 6L16 13l5 2v4a2 2 0 0 1-2 2A16 16 0 0 1 3 5a2 2 0 0 1 2-2z"/></svg>
          +61 8 8217 4592
        </li>
        <li class="contact__item">
          <svg class="contact__icon" viewBox="0 0 24 24" fill="var(--gold)"><rect x="2" y="5" width="20" height="14" rx="1"/><path d="M2 6l10 7 10-7" fill="none" stroke="#fff" stroke-width="1.5"/></svg>
          belinda@thegarbledger.example
        </li>
        <li class="contact__item">
          <svg class="contact__icon" viewBox="0 0 24 24" fill="none" stroke="var(--gold)" stroke-width="2"><circle cx="12" cy="12" r="10"/><ellipse cx="12" cy="12" rx="4" ry="10"/><path d="M2 12h20"/></svg>
          thegarbledger.example
        </li>
      </ul>
    </div>
    <div class="tagline-band">Corporate Workwear • Uniform Specialist • Personal Stylist</div>
  </section>
</body>
</html>
```